Valtrine Professional Services Website

Small website for company presence and information. Company is an IT/Telecom services company. We provide presales and installation services. Included are various company logos including color levels. Site doesn't have to use these exact colors in the logos, but should be complimentary if using different colors. It should have a professional business appearance.
Updates

My apologies for not being more responsive on the designs that have been submitted. I will be narrowing down the submissions and providing additional feedback next week. Thank you for your patience.

Project Deadline Extended
Reason: Sorry again for delays on picking designs. Work has me very busy and I've just not had the time to devote to this project. I am extending the design deadline for a few more days to give me time to make my final decisions. Thank you all for your patience. Stay tuned....

Target Market(s)

Telecom sales companies that sell Brintel telecom products.

Industry/Entity Type

Professional Service

Coding

Coded - Design and coding required

Number of Pages Required

5+ page

Font styles to use
Sans Serif

Colors
3276b5
0355a3
85abd2
85cae6
33a6d7
0692cd
ffffff

Requirements
Must have
• Professional design reflective of IT/Telecom business. A good reference website would be: http://www.quollanetworks.example/. Looking for something similar in function and presence.
Nice to have
• Rolling photos highlighting our services. Traditional navigation across the top of all pages.
Should not have
• No motion video, flashy presentation or overly confused interface.

```html
<!DOCTYPE html>
<html lang="en">
<head>
<meta charset="utf-8">
<title>Valtrine Professional Services</title>
<link href="https://fonts.googleapis.com/css2?family=Exo+2:ital,wght@0,500;0,600;0,700;0,800;1,600;1,700&family=Lato:ital,wght@0,400;0,700;1,400&display=swap" rel="stylesheet">
<style>
:root{
  --blue:#0355a3;
  --blue-mid:#3276b5;
  --sky:#33a6d7;
  --ink:#1a1a1a;
  --text:#333;
  --muted:#666;
  --line:#d5d5d5;
  --panel:#f2f2f2;
  --footer:#1b1f2a;
  --white:#fff;
}
*{margin:0;padding:0;box-sizing:border-box}
html,body{width:1200px;height:2332px;overflow:hidden}
body{position:relative;background:var(--white);font-family:"Lato",sans-serif;color:var(--text)}
a{text-decoration:none}
.abs{position:absolute}
.heading{font-family:"Exo 2",sans-serif;font-weight:800;color:var(--ink);text-transform:uppercase;white-space:nowrap}
.heading span{color:var(--blue)}
.btn{display:inline-block;background:var(--blue);color:var(--white);font-size:13px;text-transform:uppercase;border-radius:3px;text-align:center;text-decoration:none}

/* header */
.site-header{left:0;top:0;width:1200px;height:106px;border-top:2px solid var(--blue)}
.brand{left:98px;top:22px;display:flex;align-items:center;gap:12px}
.brand-mark{width:58px;height:58px;background:var(--blue)}
.brand-name{font-family:"Exo 2",sans-serif;font-weight:800;font-size:42px;line-height:38px;color:var(--blue)}
.brand-sub{font-family:"Exo 2",sans-serif;font-weight:600;font-size:13.5px;letter-spacing:2.4px;color:var(--blue)}
.topbar{left:793px;top:0;width:307px;height:34px;background:var(--blue);clip-path:polygon(0 0,100% 0,96% 100%,4% 100%);color:var(--white);display:flex;align-items:center;padding-left:30px;gap:10px;font-size:14px}
.topbar .social{display:flex;gap:8px;margin-left:22px}
.dot-icon{width:20px;height:20px;border:2px solid var(--white);border-radius:50%}
.main-nav{left:504px;top:68px;display:flex;font-family:"Exo 2",sans-serif;font-weight:700;font-size:12.5px;color:var(--ink)}
.main-nav a{color:inherit;padding:0 18px;border-left:1px solid #bbb;line-height:14px}
.main-nav a:first-child{border:0;color:var(--blue)}

/* hero */
.hero{left:0;top:106px;width:1200px;height:514px;background:radial-gradient(ellipse at 35% 30%,#8ea7c3 0%,#3e5878 35%,#1c2c44 70%,#0f1a2c 100%)}
.hero-tagline{left:100px;top:346px;font-family:"Exo 2",sans-serif;font-style:italic;font-weight:700;font-size:31px;color:var(--white)}
.hero-arrow{top:336px;width:56px;height:56px;border-radius:50%;background:rgba(0,0,0,.35);border:2px solid rgba(255,255,255,.25)}
.hero-dots{left:568px;top:578px;display:flex;gap:5px}
.hero-dots i{width:11px;height:11px;border-radius:50%;border:1.5px solid #fff}
.hero-dots i.on{background:var(--blue-mid)}

/* welcome */
.welcome-kicker{left:98px;top:664px;font-family:"Exo 2",sans-serif;font-weight:600;font-size:26px;color:var(--ink)}
.welcome-title{left:98px;top:692px;font-family:"Exo 2",sans-serif;font-weight:700;font-size:38px;color:var(--blue);white-space:nowrap}
.welcome-rule{left:98px;top:747px;width:640px;height:1px;background:var(--line)}
.welcome-copy{left:98px;top:760px;width:640px;font-size:12.6px;line-height:26.5px;color:var(--text)}
.welcome .btn{left:98px;top:960px;width:120px;line-height:36px}

.contact-card{left:783px;top:673px;width:317px;height:322px;background:var(--white);box-shadow:0 2px 8px rgba(0,0,0,.2);border-radius:3px}
.contact-card h2{height:59px;background:var(--blue);color:var(--white);text-align:center;font-family:"Exo 2",sans-serif;font-weight:700;font-size:25px;line-height:59px;border-radius:3px 3px 0 0}
.field{position:absolute;border:1px solid #ccc;border-radius:3px;font-size:11px;color:#777;padding:11px 10px;background:#fff}
.contact-card .btn{position:absolute;left:19px;top:263px;width:280px;line-height:35px;font-size:13px}

/* services */
.services{left:0;top:1049px;width:1200px;height:524px;background:var(--panel)}
.section-title{font-size:35px}
.rule-mark{height:1px;background:var(--line)}
.mark{width:20px;height:20px;border:3px solid #888;border-radius:3px;transform:rotate(45deg)}
.service-card{top:144px;width:232px;height:327px;background:var(--white);border:1px solid #ddd;text-align:center}
.service-photo{margin:4px;height:140px}
.service-card h3{font-family:"Exo 2",sans-serif;font-weight:700;font-size:19px;color:var(--blue);margin-top:20px}
.service-card p{font-size:12.5px;line-height:18px;color:var(--text);padding:0 22px;margin-top:8px}
.service-card .btn{position:absolute;left:58px;top:270px;width:112px;line-height:31px;font-size:12.5px}
.slide-arrow{top:272px}

/* events & testimonials */
.col-title{font-size:34px;top:1614px}
.pager{top:1624px;display:flex;gap:6px}
.pager i{width:24px;height:24px;border-radius:50%;border:1px solid #bbb;background:#fff}
.event{left:98px;width:477px;display:flex;gap:22px}
.event-date{width:62px;height:90px;background:var(--blue);color:#fff;border-radius:4px;text-align:center;font-family:"Exo 2",sans-serif;font-weight:700;flex:none}
.event-date b{display:block;font-size:26px;line-height:34px;margin-top:8px}
.event-date small{display:block;font-size:12px;line-height:15px}
.event h4{font-family:"Exo 2",sans-serif;font-weight:700;font-size:13px;line-height:19px;color:var(--ink)}
.event p{font-size:12.3px;line-height:18px;color:var(--text);margin-top:2px}
.event-sep{left:98px;width:477px;height:1px;background:#e2e2e2}
.quote-box{left:626px;top:1706px;width:474px;height:177px;background:#f3f3f3;border-radius:4px}
.quote-box p{font-style:italic;font-size:12.8px;line-height:25px;color:#666;text-align:justify;padding:14px 22px 0 22px;text-indent:60px}
.quote-tail{left:690px;top:1882px}
.quote-author{left:746px;top:1899px;font-family:"Exo 2",sans-serif;font-style:italic;font-weight:600;font-size:17px;color:#555}
.quote-photo{left:993px;top:1852px;width:78px;height:86px;border:3px solid #fff;box-shadow:0 1px 3px rgba(0,0,0,.3);background:linear-gradient(#c9d8e6,#5c7a99)}

/* footer */
.site-footer{left:0;top:1990px;width:1200px;height:297px;background:var(--footer);color:#fff}
.foot-col{top:44px}
.foot-col h5{font-family:"Exo 2",sans-serif;font-weight:700;font-size:18px;text-transform:uppercase;padding-bottom:10px;border-bottom:1px solid #3a3f4c;white-space:nowrap}
.foot-col h5 span{color:var(--blue-mid)}
.foot-col ul{list-style:none;font-size:13px;line-height:31px;margin-top:8px;color:#ddd}
.foot-info{font-size:14px;line-height:20px;margin-top:12px}
.foot-info strong{font-family:"Exo 2",sans-serif}
.foot-info .row{display:flex;align-items:center;gap:10px;font-size:13px;line-height:30px}
.map{width:300px;height:145px;margin-top:18px;border:3px solid #fff;background:linear-gradient(135deg,#e9e4d4,#bcd0e0 60%,#f0d68a)}
.foot-brand{left:918px;top:55px;text-align:center;width:210px}
.foot-brand .mark-sq{width:56px;height:56px;background:#d0d0d0;margin:0 auto 12px}
.foot-brand b{display:block;font-family:"Exo 2",sans-serif;font-weight:800;font-size:34px;line-height:36px}
.foot-brand small{font-family:"Exo 2",sans-serif;font-weight:600;font-size:11px;letter-spacing:2px}
.foot-brand .social{display:flex;justify-content:center;gap:12px;margin-top:26px}
.foot-brand .dot-icon{width:26px;height:26px}
.copyright{left:0;top:2287px;width:1200px;height:45px;background:var(--blue);color:#fff;text-align:center;font-size:14px;line-height:45px}
</style>
</head>
<body>

<header class="site-header abs">
  <div class="brand abs">
    <div class="brand-mark"></div>
    <div>
      <div class="brand-name">VALTRINE</div>
      <div class="brand-sub">PROFESSIONAL SERVICES</div>
    </div>
  </div>
  <div class="topbar abs">
    <svg width="16" height="16" viewBox="0 0 24 24"><path fill="#fff" d="M6.6 10.8a15 15 0 0 0 6.6 6.6l2.2-2.2c.3-.3.7-.4 1-.2 1.1.4 2.3.6 3.6.6.6 0 1 .4 1 1V20c0 .6-.4 1-1 1C10.6 21 3 13.4 3 4c0-.6.4-1 1-1h3.5c.6 0 1 .4 1 1 0 1.3.2 2.5.6 3.6.1.3 0 .7-.2 1z"/></svg>
    <span>(123) 456-7890</span>
    <div class="social"><i class="dot-icon"></i><i class="dot-icon"></i><i class="dot-icon"></i></div>
  </div>
  <nav class="main-nav abs">
    <a href="#">HOME</a><a href="#">COMPANY PROFILE</a><a href="#">OUR SERVICES</a><a href="#">EVENTS</a><a href="#">CONTACT US</a>
  </nav>
</header>

<section class="hero abs" role="img" aria-label="Photo of network cables against glowing fibre optic lights"></section>
<div class="hero-tagline abs">Expertise. Insight. Experience.</div>
<div class="hero-arrow abs" style="left:30px"><svg width="52" height="52" viewBox="0 0 52 52"><path d="M30 16 20 26l10 10" stroke="#fff" stroke-width="2" fill="none"/></svg></div>
<div class="hero-arrow abs" style="left:1112px"><svg width="52" height="52" viewBox="0 0 52 52"><path d="M22 16l10 10-10 10" stroke="#fff" stroke-width="2" fill="none"/></svg></div>
<div class="hero-dots abs"><i></i><i class="on"></i><i></i><i></i></div>

<section class="welcome">
  <div class="welcome-kicker abs">Welcome To</div>
  <h1 class="welcome-title abs">VALTRINE PROFESSIONAL SERVICES</h1>
  <div class="welcome-rule abs"></div>
  <p class="welcome-copy abs">Lorem ipsum dolor sit amet, consectetuer adipiscing elit, sed diam nonummy nibh euismod tincidunt ut laoreet dolore magna aliquam erat volutpat. Ut wisi enim ad minim veniam, quis nostrud exerci tation ullamcorper st lobortis nisl ut aliquip ex ea commodo consequat. Duis autem vel eum iriure dolor in hendrerit in vulp velit es molestie consequat, vel illum dolore eu feugiat nulla facilisis at vero eros et accumsan et iusto odio dignissim qui blandit praesent luptatum zzril delenit augue duis dolore te feugait nulla facilisi. Lorem ipsum dolor sit amet, consectetuer adipiscing elit, sed diam nonummy nibh euismod tincidunt ut laoreet dolore magna aliqua volutpat. Ut wisi enim ad minim veniam, quis nostrud exerci tation ullamcorper.</p>
  <a class="btn abs" href="#">Learn More</a>

  <form class="contact-card abs">
    <h2>CONTACT US</h2>
    <div class="field" style="left:19px;top:78px;width:136px;height:37px">Name</div>
    <div class="field" style="left:164px;top:78px;width:136px;height:37px">Phone</div>
    <div class="field" style="left:19px;top:126px;width:136px;height:37px">Email</div>
    <div class="field" style="left:164px;top:126px;width:136px;height:37px">Company</div>
    <div class="field" style="left:19px;top:174px;width:281px;height:73px">Comments</div>
    <div class="btn">Submit</div>
  </form>
</section>

<section class="services abs">
  <h2 class="heading section-title abs" style="left:0;width:1200px;text-align:center;top:40px">Our <span>Services</span></h2>
  <div class="rule-mark abs" style="left:98px;top:103px;width:480px"></div>
  <div class="rule-mark abs" style="left:622px;top:103px;width:478px"></div>
  <div class="mark abs" style="left:590px;top:93px"></div>

  <svg class="slide-arrow abs" style="left:46px" width="34" height="66" viewBox="0 0 34 66"><path d="M32 2 2 33l30 31" stroke="#777" stroke-width="1.5" fill="none"/></svg>
  <svg class="slide-arrow abs" style="left:1118px" width="34" height="66" viewBox="0 0 34 66"><path d="M2 2l30 31L2 64" stroke="#777" stroke-width="1.5" fill="none"/></svg>

  <article class="service-card abs" style="left:98px">
    <div class="service-photo" role="img" aria-label="Photo of a businessman drawing a cloud network diagram" style="background:linear-gradient(135deg,#1f4f8a,#0d2546)"></div>
    <h3>Managed Services</h3>
    <p>Lorem ipsum dolor sit amet, consectetuer adipiscing elit, sed diam nonummy nibh...</p>
    <a class="btn" href="#">Learn More</a>
  </article>
  <article class="service-card abs" style="left:356px">
    <div class="service-photo" role="img" aria-label="Photo of people holding question mark signs" style="background:linear-gradient(180deg,#e8eef4,#7ea8cc)"></div>
    <h3>Readiness Assessment</h3>
    <p>Lorem ipsum dolor sit amet, consectetuer adipiscing elit, sed diam nonummy nibh...</p>
    <a class="btn" href="#">Learn More</a>
  </article>
  <article class="service-card abs" style="left:614px">
    <div class="service-photo" role="img" aria-label="Photo of a hand touching a tablet with a global network" style="background:linear-gradient(135deg,#2c5d8f,#6fb6e4 60%,#c7d7e4)"></div>
    <h3>Refurbish &amp; Buyback</h3>
    <p>Lorem ipsum dolor sit amet, consectetuer adipiscing elit, sed diam nonummy nibh...</p>
    <a class="btn" href="#">Learn More</a>
  </article>
  <article class="service-card abs" style="left:870px">
    <div class="service-photo" role="img" aria-label="Photo of hands joining puzzle pieces" style="background:linear-gradient(135deg,#4a4a4a,#9a9a9a 50%,#3a3a3a)"></div>
    <h3>Implementation</h3>
    <p>Lorem ipsum dolor sit amet, consectetuer adipiscing elit, sed diam nonummy nibh...</p>
    <a class="btn" href="#">Learn More</a>
  </article>
</section>

<section class="events">
  <h2 class="heading col-title abs" style="left:98px">Events <span>News</span></h2>
  <div class="pager abs" style="left:514px"><i></i><i></i></div>
  <div class="mark abs" style="left:101px;top:1666px;width:17px;height:17px"></div>
  <div class="rule-mark abs" style="left:134px;top:1675px;width:441px"></div>

  <article class="event abs" style="top:1705px">
    <div class="event-date"><b>22</b><small>JAN</small><small>2017</small></div>
    <div><h4>Lorem ipsum dolor sit amet, consectetuer adipiscing elit<br>Wisi enim and minim.</h4>
    <p>Sed diam nonummy nibh euismod tincidunt ut laoreet dolore magna aliquam erat volutpat. Ut wisi enim ad minim veniam, quis nostrud exerci tation ullamcorper st lobortis nisl ut aliquip.</p></div>
  </article>
  <div class="event-sep abs" style="top:1810px"></div>
  <article class="event abs" style="top:1826px">
    <div class="event-date"><b>22</b><small>JAN</small><small>2017</small></div>
    <div><h4>Lorem ipsum dolor sit amet, consectetuer adipiscing elit<br>Wisi enim and minim.</h4>
    <p>Sed diam nonummy nibh euismod tincidunt ut laoreet dolore magna aliquam erat volutpat. Ut wisi enim ad minim veniam, quis nostrud exerci tation ullamcorper st lobortis nisl ut aliquip.</p></div>
  </article>
</section>

<section class="testimonials">
  <h2 class="heading col-title abs" style="left:621px">Client <span>Testimonials</span></h2>
  <div class="pager abs" style="left:1039px"><i></i><i></i></div>
  <div class="mark abs" style="left:628px;top:1666px;width:17px;height:17px"></div>
  <div class="rule-mark abs" style="left:661px;top:1675px;width:439px"></div>
  <blockquote class="quote-box abs">
    <p>Fusce elementum, nulla vel pellentes consequat, ante nulla hendrerit arcu, ac tincidunt mauris lacus sed leo. vamus suscipit molestie vestibulum. Lorem ipsum dolor sit amet, Fusce elementum, nulla vel pellentes consequat, ante nulla hendrerit arcu, ac tincidunt mauris lacus sed leo. vamus suscipit molestie vestibulum.</p>
  </blockquote>
  <svg class="quote-tail abs" width="40" height="36" viewBox="0 0 40 36"><path d="M0 0h40L36 36z" fill="#f3f3f3"/></svg>
  <div class="quote-author abs">-Nulla vel pellentes</div>
  <div class="quote-photo abs" role="img" aria-label="Portrait photo of the client"></div>
</section>

<footer class="site-footer abs">
  <div class="foot-col abs" style="left:100px;width:137px">
    <h5>Quick <span>Links</span></h5>
    <ul><li>• Home</li><li>• Company Profile</li><li>• Our Services</li><li>• Events</li><li>• Contact Us</li></ul>
  </div>
  <div class="foot-col abs" style="left:286px;width:246px">
    <h5>Contact <span>Information</span></h5>
    <div class="foot-info">
      <strong>Valtrine Professional Services</strong><br>Lorem ipsum dolor sit amet,<br>consectetuer, NC1234
      <div class="row" style="margin-top:8px"><svg width="12" height="12" viewBox="0 0 24 24"><path fill="#fff" d="M6.6 10.8a15 15 0 0 0 6.6 6.6l2.2-2.2c.3-.3.7-.4 1-.2 1.1.4 2.3.6 3.6.6.6 0 1 .4 1 1V20c0 .6-.4 1-1 1C10.6 21 3 13.4 3 4c0-.6.4-1 1-1h3.5c.6 0 1 .4 1 1 0 1.3.2 2.5.6 3.6.1.3 0 .7-.2 1z"/></svg>(123) 456-7890</div>
      <div class="row"><svg width="13" height="12" viewBox="0 0 24 22"><path fill="#fff" d="M6 0h12v6H6zM2 7h20v10h-4v5H6v-5H2zM8 14v6h8v-6z"/></svg>(123) 456-7890</div>
      <div class="row"><svg width="13" height="10" viewBox="0 0 24 18"><path fill="#fff" d="M0 0h24v18H0zM2 2v1l10 7 10-7V2z"/></svg>info@valtrineservices.example</div>
    </div>
  </div>
  <div class="foot-col abs" style="left:579px;width:300px">
    <h5>Location <span>Map</span></h5>
    <div class="map" role="img" aria-label="Street map showing the office location"></div>
  </div>
  <div class="foot-brand abs">
    <div class="mark-sq"></div>
    <b>VALTRINE</b>
    <small>PROFESSIONAL SERVICES</small>
    <div class="social"><i class="dot-icon"></i><i class="dot-icon"></i><i class="dot-icon"></i></div>
  </div>
</footer>
<div class="copyright abs">Copyright © 2017. Valtrine Professional Services. All Right Reserved</div>

</body>
</html>
```